LunaGowns.com Banner AD

We are looking for some talented creators to create for us a banner ad for our online clothing store that specializes in dresses. We are looking for a fresh, clean, and sleek KORA, P&Q, and Glint appeal- clean, modern and sophisticated.

We would like for the final project to appear professionally done, we've had projects completed by several talent out there that did not capture our image, and let's just say it was too cluttered and appeared as if a high school editor had completed it.

I have attached a few files for you to reference, I have File 1, 2, 3, 8 and the P&Q photos as examples of what we DO like.

I have attached File 5, which is the work of one the designers that was working on this project. Although it is very simple and gets the point across, it doesn't come across like a magazine editorial.

I have attached File 6, that is the main photo we wish to use for our banner.

I have attached File 7, which is what a creator had done for us via Brevora.com, that is a good example of what we do NOT want.

That is about sums it up! I hope the examples are useful tools for you!

Hi Designers!

Thank you so much for your submissions! I enjoy viewing each and every one of them! Please view my update on what I am looking for, I have made some adjustments and have added a few more examples to reference, I have made my direction a bit more clearer. Because it seems some designers are not quite understanding my direction. I know you all have amazing talent and I am hoping to see something I am looking for and I love soon! If you have any other questions, please don't hesitate to ask! 

Target Market(s)

Our company targets women of all ages, we carry dresses that cater to every occasion, whether its an older woman looking for a dress to attend a wedding or a teenager looking for a prom dress. We want our front page banner to appear fresh, clean, with a feminine touch, we want to stray from tacky (gradients, etc..) and keep it classy all while maintaining that magazine editorial element, we want to be more fashion focused, like Glint. We want this project to appear professionally done. Our desired concept is something out of a magazine editorial, not too much going on, while shifting focus more on the dress itself than a design element like flowers or spring backgrounds.

Industry/Entity Type

High School

Requirements
Must have
• We want a glint fashion appeal, magazine editorial type of look. The phrases below should be included"

"New Season New Sexy Dresses"

"Free U.S shipping on orders $75+"
"Shop our sales up to 60% off"

All of the other phrases do not need to be included. Also, Do not include the parenthesis.
Should not have
• Only include the photo I've attached that appears solo. Please do not include the other 3 dresses that is displayed in a banner that was created for us by another designer. (that is provided as an example only)

```html
<!DOCTYPE html>
<html lang="en">
<head>
<meta charset="utf-8">
<title>LunaGowns.com Banner</title>
<link rel="stylesheet" href="https://fonts.googleapis.com/css2?family=Oswald:wght@400;500&family=Arimo&display=swap">
<style>
  :root {
    --page: #ffffff;
    --paper-warm: #d8d2ba;
    --paper-light: #eef0e3;
    --paper-mid: #e3e4d2;
    --ink-soft: #5a5a5a;
    --ink-strong: #3c3c3c;
    --ink-body: #454545;
    --accent: #de3f92;
    --shadow: rgba(0, 0, 0, 0.22);
    --photo-top: #e9e7dc;
    --photo-skin: #d9a98a;
    --photo-pink: #e96aa8;
    --photo-violet: #8b78c4;
  }
  * { margin: 0; padding: 0; box-sizing: border-box; }
  html, body {
    width: 1200px;
    height: 1000px;
    overflow: hidden;
    background: var(--page);
  }
  .banner {
    position: absolute;
    left: 186px;
    top: 132px;
    width: 827px;
    height: 719px;
    background:
      linear-gradient(100deg, var(--paper-warm) 0%, var(--paper-light) 35%, var(--paper-mid) 60%, var(--paper-light) 100%);
    box-shadow: 0 14px 24px -6px var(--shadow);
    overflow: hidden;
  }
  .model-photo {
    position: absolute;
    left: 470px;
    top: 0;
    width: 357px;
    height: 719px;
    background:
      linear-gradient(180deg, var(--photo-top) 0%, var(--photo-skin) 22%, var(--photo-pink) 48%, var(--photo-violet) 72%, var(--photo-pink) 88%, var(--photo-skin) 100%);
    opacity: 0.85;
    -webkit-mask-image: linear-gradient(90deg, transparent 0%, #000 18%);
            mask-image: linear-gradient(90deg, transparent 0%, #000 18%);
  }
  .headline {
    position: absolute;
    left: 57px;
    top: 112px;
    font-family: "Oswald", sans-serif;
    font-weight: 500;
    font-size: 43px;
    line-height: 48px;
    letter-spacing: 1.5px;
    text-transform: uppercase;
  }
  .headline__line--light { color: var(--ink-soft); display: block; }
  .headline__line--strong { color: var(--ink-strong); display: block; }
  .sale-box {
    position: absolute;
    left: 55px;
    top: 442px;
    width: 158px;
    height: 162px;
    border: 2px solid var(--accent);
    color: var(--accent);
    font-family: "Oswald", sans-serif;
    font-weight: 500;
    text-transform: uppercase;
    text-align: center;
  }
  .sale-box__lead {
    margin-top: 14px;
    font-size: 21px;
    line-height: 30px;
    letter-spacing: 0.5px;
  }
  .sale-box__figure {
    font-size: 72px;
    line-height: 68px;
    margin-top: 2px;
  }
  .shipping-note {
    position: absolute;
    left: 52px;
    top: 628px;
    font-family: "Arimo", sans-serif;
    font-size: 28px;
    color: var(--ink-body);
    white-space: nowrap;
  }
</style>
</head>
<body>
  <section class="banner" aria-label="LunaGowns.com new season banner">
    <div class="model-photo" role="img" aria-label="Photo of a smiling woman with long wavy hair, hands on hips, wearing a fitted sleeveless pink and violet watercolour-print dress with a front cut-out"></div>

    <h1 class="headline">
      <span class="headline__line--light">New Season</span>
      <span class="headline__line--strong">New Sexy Dresses</span>
    </h1>

    <div class="sale-box">
      <p class="sale-box__lead">Shop our<br>sales up to</p>
      <p class="sale-box__figure">60%</p>
    </div>

    <p class="shipping-note">FREE US Shipping on orders $75+</p>
  </section>
</body>
</html>
```